Wander Main Street Merchants Pinebrook Event

We are hosting a Wander Main Street Merchants Pinebrook event in conjunction with Northwind Credit's Hometown Harvest Weekend. Participants will be given a passport to get stamped at participating businesses. They will be entered to win $$ prizes! I have attached a Word document with the info that needs to be included.

Target Market(s)

Christmas shoppers, mainly women.

Colors
f04a50
31b7a3

Requirements
Must have
• The info attached. Christmas or holiday images.

```html
<!DOCTYPE html>
<html lang="en">
<head>
<meta charset="utf-8">
<title>Wander Main Street Merchants Pinebrook</title>
<link rel="stylesheet" href="https://fonts.googleapis.com/css2?family=Poppins:ital,wght@0,300;0,400;0,500;0,600;0,700;0,800;1,400&display=swap">
<style>
  :root {
    --teal: #31b7a3;
    --red: #f04a50;
    --gray: #7d7d7d;
    --gray-dark: #6b6b6b;
    --band: #8e8e8e;
    --green: #3e7b35;
    --paper: #ffffff;
    --stage: #cdcdcd;
  }
  * { margin: 0; padding: 0; box-sizing: border-box; }
  html, body { width: 1200px; height: 1200px; overflow: hidden; }
  body { background: var(--stage); font-family: "Poppins", sans-serif; }

  .flyer {
    position: absolute; left: 176px; top: 0;
    width: 848px; height: 1200px;
    background: var(--paper); overflow: hidden;
  }
  .abs { position: absolute; }

  .brand {
    left: 0; width: 848px; top: 48px; text-align: center;
    font-size: 34px; font-weight: 400; color: var(--green); letter-spacing: 1px;
  }
  .hero-photo { left: 0; top: 170px; }
  .headline {
    left: 0; width: 848px; top: 140px; text-align: center;
    font-size: 38px; font-weight: 300; color: var(--gray); letter-spacing: 0.5px;
  }
  .date-month { left: 153px; top: 222px; font-size: 42px; font-weight: 400; color: var(--gray-dark); line-height: 1; }
  .date-day { left: 150px; top: 262px; font-size: 98px; font-weight: 700; color: var(--teal); line-height: 1; letter-spacing: -2px; }
  .date-year {
    left: 402px; top: 340px; font-size: 52px; font-weight: 700; color: var(--gray-dark);
    transform: rotate(-90deg); transform-origin: left top; line-height: 1;
  }
  .time-box { left: 474px; top: 225px; width: 218px; height: 117px; }
  .time-text {
    left: 474px; top: 234px; width: 218px; text-align: center;
    color: #fff; font-weight: 700; font-size: 33px; line-height: 1.1;
  }
  .time-dash { display: block; font-size: 18px; line-height: 0.6; }

  .prize { top: 695px; width: 280px; height: 84px; }
  .prize-left { left: 78px; }
  .prize-right { left: 490px; }
  .prize-frame { position: absolute; left: 0; top: 0; }
  .prize-label {
    position: absolute; left: 0; top: 0; width: 88px; height: 84px;
    color: #fff; font-weight: 800; font-size: 19px; line-height: 1.05;
    display: flex; align-items: center; justify-content: center; text-align: center;
  }
  .prize-left .prize-label { background: var(--teal); }
  .prize-right .prize-label { background: var(--red); }
  .prize-amount {
    position: absolute; left: 88px; right: 0; top: 0; height: 84px;
    display: flex; flex-direction: column; align-items: center; justify-content: center;
    color: var(--gray-dark); font-weight: 700; font-size: 48px; line-height: 1;
  }
  .prize-note { font-size: 14px; font-weight: 400; color: var(--gray); margin-bottom: 2px; }
  .prize-caption {
    top: 797px; width: 290px; font-size: 13px; font-style: italic; color: var(--gray); line-height: 1.5;
  }
  .divider { left: 424px; top: 688px; width: 1px; height: 124px; background: #d2d2d2; }

  .santa-band { left: 0; top: 846px; width: 848px; height: 37px; background: var(--band); }
  .santa-band-text { left: 78px; top: 853px; color: #fff; font-weight: 700; font-size: 17px; }

  .contact-lead { left: 78px; top: 906px; font-size: 18px; color: var(--gray); font-weight: 400; }
  .contact-name { left: 78px; top: 932px; font-size: 18px; color: var(--red); font-weight: 700; }
  .contact-phone { left: 78px; top: 957px; display: flex; align-items: center; gap: 8px;
    font-size: 28px; font-weight: 700; color: var(--gray-dark); }
  .fine-print { left: 78px; top: 1011px; width: 340px; font-size: 9.5px; font-style: italic; color: var(--gray); line-height: 1.55; }

  .sponsor-band { left: 0; top: 1050px; width: 848px; height: 150px; background: var(--teal); }
  .sponsor-title { left: 78px; top: 1066px; color: #fff; font-weight: 700; font-size: 18px; }
  .sponsor-list { left: 78px; top: 1098px; color: #fff; font-size: 10.5px; line-height: 22px; }
  .sponsor-list span + span { border-left: 1px solid #fff; padding-left: 4px; margin-left: 3px; }

  .santa-photo {
    left: 466px; top: 856px; width: 382px; height: 344px;
    background: linear-gradient(160deg, #f3f0ec 0%, #e6d8cc 30%, #d83a36 55%, #c9302e 100%);
    border-top-left-radius: 120px;
  }
</style>
</head>
<body>
<main class="flyer">
  <svg class="abs hero-photo" width="848" height="510" viewBox="0 170 848 510" role="img" aria-label="Blurred holiday shoppers walking through a lit street with warm bokeh lights">
    <defs>
      <linearGradient id="warm" x1="0" y1="0" x2="1" y2="0">
        <stop offset="0" stop-color="#d9b98c"/>
        <stop offset="0.35" stop-color="#f1e4cf"/>
        <stop offset="0.6" stop-color="#fbf5ea"/>
        <stop offset="1" stop-color="#d7ae6e"/>
      </linearGradient>
      <linearGradient id="fade" x1="0" y1="0" x2="0" y2="1">
        <stop offset="0" stop-color="#fff" stop-opacity="1"/>
        <stop offset="0.25" stop-color="#fff" stop-opacity="0.2"/>
        <stop offset="1" stop-color="#fff" stop-opacity="0"/>
      </linearGradient>
    </defs>
    <path d="M0 179 H848 V462 Q430 880 0 470 Z" fill="url(#warm)"/>
    <path d="M0 179 H848 V462 Q430 880 0 470 Z" fill="url(#fade)"/>
  </svg>

  <div class="abs brand">Downtown Pinebrook</div>
  <h1 class="abs headline">WANDER MAIN STREET MERCHANTS</h1>

  <div class="abs date-month">NOVEMBER</div>
  <div class="abs date-day">27TH</div>
  <div class="abs date-year">2021</div>

  <svg class="abs time-box" viewBox="0 0 218 117">
    <polygon points="0,0 196,0 218,22 218,117 0,117" fill="var(--teal)"/>
  </svg>
  <div class="abs time-text">10:00 A.M.<span class="time-dash">–</span>2:00 P.M.</div>

  <div class="abs prize prize-left">
    <svg class="prize-frame" width="280" height="84" viewBox="0 0 280 84">
      <polygon points="0.5,0.5 252,0.5 279.5,28 279.5,83.5 0.5,83.5" fill="#fff" stroke="#a8a8a8"/>
    </svg>
    <div class="prize-label">ENTER<br>TO<br>WIN</div>
    <div class="prize-amount">$500</div>
  </div>
  <p class="abs prize-caption" style="left:78px">in Shopping Dollars and other gift giveaways!*</p>

  <div class="abs divider"></div>

  <div class="abs prize prize-right">
    <svg class="prize-frame" width="280" height="84" viewBox="0 0 280 84">
      <polygon points="0.5,0.5 252,0.5 279.5,28 279.5,83.5 0.5,83.5" fill="#fff" stroke="#a8a8a8"/>
    </svg>
    <div class="prize-label">ENTER<br>TO<br>WIN</div>
    <div class="prize-amount"><span class="prize-note">ONE of FIVE</span>$250</div>
  </div>
  <p class="abs prize-caption" style="left:490px">Shopping Dollars! Pick up your FREE Tote &amp; Passport at the Depot</p>

  <div class="abs santa-band"></div>
  <div class="abs santa-band-text">GET YOUR PICTURES WITH PINEBROOK'S SANTA CLAUS</div>

  <div class="abs contact-lead">FOR MORE INFORMATION CONTACT</div>
  <div class="abs contact-name">CARLA BRENNER</div>
  <div class="abs contact-phone">
    <svg width="28" height="28" viewBox="0 0 28 28" aria-hidden="true">
      <circle cx="14" cy="14" r="14" fill="var(--red)"/>
      <path d="M9.5 7.5c.8-.5 1.6-.3 2 .4l1.3 2.3c.4.7.2 1.4-.4 1.8l-.9.6c.7 1.8 2 3.2 3.8 4.1l.6-.9c.4-.6 1.2-.8 1.8-.4l2.3 1.3c.7.4.9 1.3.4 2l-.8 1c-.7.8-1.8 1.1-2.8.7-4.2-1.6-7.3-4.7-8.8-8.9-.4-1 0-2.1.8-2.8z" fill="#fff"/>
    </svg>
    555-014-2270
  </div>
  <p class="abs fine-print">*Eligible to be entered to win when stamps from all participating stores reflected on Wander Main Street Merchants Passport</p>

  <div class="abs sponsor-band"></div>
  <div class="abs sponsor-title">SPONSORED BY</div>
  <div class="abs sponsor-list">
    <div><span>Evening Porch Series</span><span>Valley Orchard Festival</span><span>R. Dell's Design Studio</span></div>
    <div><span>Laurel County Chamber &amp; Tourism</span><span>Owen Marsh Photography</span></div>
    <div><span>Riverbend Power Cooperative</span><span>Pinebrook Downtown Development</span></div>
    <div><span>The Pinebrook Ledger</span><span>WPBK 98.7 FM</span><span>Pinebrook's Santa Claus</span></div>
  </div>

  <div class="abs santa-photo" role="img" aria-label="Santa Claus posing for a selfie with a smiling shopper in a holiday hat"></div>
</main>
</body>
</html>
```